Logo needed for business card

Velquist Pty Ltd is in the business of healthcare and ecommerce.

We own and manage pharmacies and online health ecomerce sites.

We provide ecommerce consultants for companies looking for an ecommerce business startegy.

Think of it as the umbrella under which several healthcare brands may sit.

When I think of Velquist, I visulaise slick black/metalic colours, so please stay away from the common blue and green colours that seem to be so popular in this field.

Target Market(s)

CEOs and COOs

Industry/Entity Type

Healthcare

Contact Information for Business Card

Tessa Lindqvist
Director
Velquist Pty Ltd
4/362 Fennick Pde
Brellton, NSW 2148

Requirements
Must have
• Design must have scope to be implemented on the company's website and letterheads etc.

```html
<!DOCTYPE html>
<html lang="en">
<head>
<meta charset="utf-8">
<title>Velquist Pty Ltd — Business Card</title>
<link rel="stylesheet" href="https://fonts.googleapis.com/css2?family=Poppins:wght@300;400;600&display=swap">
<style>
  :root {
    --page: #ffffff;
    --charcoal-deep: #0d0e10;
    --charcoal-mid: #2a2d31;
    --steel-light: #8a9099;
    --steel-sheen: #c9ced5;
    --brand-metal: #d8bc72;
    --text-silver: #eef0f3;
    --mark-silver: #e4e7eb;
  }
  html, body {
    margin: 0;
    padding: 0;
    width: 1200px;
    height: 1000px;
    overflow: hidden;
    background: var(--page);
    font-family: "Poppins", sans-serif;
  }
  .canvas {
    position: relative;
    width: 1200px;
    height: 1000px;
  }
  .card {
    position: absolute;
    left: 122px;
    top: 181px;
    width: 961px;
    height: 592px;
    overflow: hidden;
    background:
      radial-gradient(ellipse 420px 380px at 960px 250px, rgba(201, 206, 213, 0.55), rgba(201, 206, 213, 0) 70%),
      radial-gradient(ellipse 520px 420px at 560px 360px, rgba(110, 116, 124, 0.45), rgba(110, 116, 124, 0) 75%),
      linear-gradient(100deg, var(--charcoal-deep) 0%, #16181b 18%, var(--charcoal-mid) 52%, #4a4f56 78%, var(--steel-light) 100%);
  }
  .card::after {
    content: "";
    position: absolute;
    inset: 0;
    background: linear-gradient(180deg, rgba(0, 0, 0, 0.22) 0%, rgba(0, 0, 0, 0) 30%, rgba(0, 0, 0, 0) 75%, rgba(0, 0, 0, 0.2) 100%);
    pointer-events: none;
  }
  .backdrop-disc {
    position: absolute;
    left: -50px;
    top: 128px;
    width: 360px;
    height: 360px;
    border-radius: 50%;
    background: rgba(201, 206, 213, 0.10);
  }
  .holder {
    position: absolute;
    left: 69px;
    top: 52px;
    color: var(--text-silver);
    z-index: 1;
  }
  .holder-name {
    margin: 0;
    font-size: 29px;
    font-weight: 400;
    line-height: 1.2;
    letter-spacing: 0.2px;
  }
  .holder-role {
    margin: 2px 0 0;
    font-size: 25px;
    font-weight: 300;
    line-height: 1.2;
  }
  .brand-disc {
    position: absolute;
    left: 236px;
    top: 355px;
    width: 120px;
    height: 120px;
    border-radius: 50%;
    background: var(--mark-silver);
    z-index: 1;
  }
  .company {
    position: absolute;
    left: 381px;
    top: 340px;
    z-index: 1;
  }
  .company-name {
    margin: 0;
    font-size: 41px;
    font-weight: 600;
    line-height: 1.1;
    color: var(--brand-metal);
    letter-spacing: 0.3px;
  }
  .company-address {
    margin: 10px 0 0;
    font-size: 29px;
    font-weight: 300;
    line-height: 1.3;
    color: var(--text-silver);
    font-style: normal;
  }
</style>
</head>
<body>
  <div class="canvas">
    <section class="card" role="img" aria-label="Business card on a brushed charcoal background shading to steel grey">
      <div class="backdrop-disc"></div>
      <div class="holder">
        <p class="holder-name">Tessa Lindqvist</p>
        <p class="holder-role">Director</p>
      </div>
      <div class="brand-disc"></div>
      <div class="company">
        <p class="company-name">velquist pty ltd</p>
        <address class="company-address">4/362 Fennick Pde Brellton,<br>NSW 2148</address>
      </div>
    </section>
  </div>
</body>
</html>
```